Book Cover Design Project

I need a book cover for a book that we will be releasing in the next few months.

It is a business book aimed at small businesses and people who want to escape the 9 - 5 and start their own business.

We want it to look similar to: http://www.tolvanbrook.example/wp-content/uploads/2010/03/fold-up.jpg and also the book designs that I have uploaded images for.

I quite like the grey / charcoal background and the bright lime green colours from the Quiet Harbor logo that I have attached. However, anything bright would be good - I am prepared to be flexible with colours. The books I have attached are a high impact as well - being bright blue with white black font with a really cool font.

The book is titled:

The Lantern Shop Plan

By Dale Vortan

Still thinking of the tagline, for now just use "Start an Online Business in no time at all"

Room for a quote/testimonial on the front of the book at the bottom, and as well on the back.

For the back cover text just use dummy text and my photo that is attached for now as well.

Barcode ISBN on the back at the bottom - price will be $19.95

Needs to be in PSD so we can change the text from our end.

I really want to get a good template made that I can edit the text for as we are still developing the book, but I want to get the book cover done so I can start advertising that it will be arriving soon.

There will probably be alterations that I need help with later down the track so looking to work with someone closely on this, and I will pay you for any extra time down the track..

Sizes will probably be around: I think 20.5cm tall and 14cm wide would be good..

Not sure how thick for the spine, it will depend on how many words get cut off, but as an estimate probably 1.5CM..
Updates

Just added some more detail to the brief.. Please read it carefully.

Target Market(s)

small business owners, professionals who want to start their own business, soon to be entrepreneurs, entrepreneurs

Industry/Entity Type

Advertising

Requirements
Must have
• The Lantern Shop Plan

and Dale Vortan must be prominent.

Tag line should be look cool under the title.

Must be very modern and cool. Needs to catch people's eyes so needs to be really punchy.

Nice to have
• Maybe a clock or stopwatch icon would be cool to add in there so it isn't just plain.. Similar to like how the books have a cool icon with them that I have attached in the uploaded images.
Should not have
• I like simplicity, artistic and very high impact. It really needs to draw you in and catch your eye.

Don't use plain boring fonts. Although I like simplicity slick design is very important - I dont want it to be boring - it has to look high quality and expensive. Therefore do not use fonts like Arial, Times New Roman those really boring fonts that make it look cheap. If I was going to do something like that then I might as well do it myself.

If you want to see the quality of things that I am usually involved with look at the artwork for one of my events that I run called Daybreaker: http://www.daybreaker.example/daybreaker-festival-anthems-ft-loomsparrow-harvest-night-eve-metro-report/

That will give you an idea of what type of quality things that I am involved with, so you need to be up for the task..

```html
<!DOCTYPE html>
<html lang="en">
<head>
<meta charset="utf-8">
<title>The Lantern Shop Plan — Dale Vortan</title>
<link rel="stylesheet" href="https://fonts.googleapis.com/css2?family=Michroma&display=swap">
<style>
  :root {
    --navy: #07073f;
    --navy-soft: rgba(7, 7, 63, 0.78);
    --navy-fade: rgba(7, 7, 63, 0);
    --sky-light: #b6cff6;
    --sky-mid: #9ebdf0;
    --sky-edge: #82a9e7;
    --white: #ffffff;
    --rim: #dce8fb;
  }
  html, body {
    margin: 0;
    padding: 0;
    width: 820px;
    height: 1200px;
    overflow: hidden;
    background: var(--white);
  }
  .cover {
    position: relative;
    width: 820px;
    height: 1200px;
    overflow: hidden;
    background: radial-gradient(ellipse 75% 62% at 42% 52%, var(--sky-light) 0%, var(--sky-mid) 58%, var(--sky-edge) 100%);
    font-family: "Michroma", sans-serif;
    color: var(--navy);
  }
  .author-band {
    position: absolute;
    top: 0;
    left: 0;
    width: 820px;
    height: 46px;
    background: var(--navy);
    display: flex;
    align-items: center;
    justify-content: center;
  }
  .author {
    margin: 0;
    color: var(--white);
    font-size: 24px;
    letter-spacing: 1px;
    font-weight: 400;
    -webkit-text-stroke: 0.6px var(--white);
  }
  .title {
    position: absolute;
    top: 192px;
    left: 0;
    width: 820px;
    margin: 0;
    text-align: center;
    font-size: 35px;
    font-weight: 400;
    white-space: nowrap;
    letter-spacing: 1px;
    -webkit-text-stroke: 1px var(--navy);
  }
  .world-map {
    position: absolute;
    top: 315px;
    left: 35px;
    width: 750px;
    height: 365px;
    background: radial-gradient(ellipse 50% 50% at 50% 50%, var(--navy-soft) 0%, rgba(7, 7, 63, 0.55) 55%, var(--navy-fade) 100%);
  }
  .tagline {
    position: absolute;
    top: 741px;
    left: 0;
    width: 820px;
    margin: 0;
    text-align: center;
    font-size: 25.5px;
    line-height: 33px;
    font-weight: 400;
    white-space: nowrap;
    -webkit-text-stroke: 0.6px var(--navy);
  }
  .base-wave {
    position: absolute;
    left: 0;
    top: 1030px;
    width: 820px;
    height: 170px;
  }
</style>
</head>
<body>
  <main class="cover">
    <header class="author-band">
      <p class="author">DALE VORTAN</p>
    </header>

    <h1 class="title">THE LANTERN SHOP PLAN</h1>

    <div class="world-map" role="img" aria-label="Silhouette map of the world's continents in dark navy"></div>

    <p class="tagline">START AN ONLINE BUSINESS<br>IN NO TIME AT ALL</p>

    <svg class="base-wave" viewBox="0 0 820 170" aria-hidden="true">
      <path d="M0 8 Q410 156 820 8 L820 170 L0 170 Z" fill="var(--rim)" opacity="0.9"/>
      <path d="M0 22 Q410 170 820 22 L820 170 L0 170 Z" fill="var(--navy)"/>
    </svg>
  </main>
</body>
</html>
```